Design Short Report for Non Governmental Organisation

We need a graphic designer to help us turn a basic Word report (1 graph, 10 pages of text) into an engaging public document. The content is pretty straightforward and we can provide all the imagery necessary.

Few design restrictions apply:

Font: Trebuchet
Colors: black, white and green (Pantone 38, R (105), G (190), B (40)

Attached you will find the full copy of the report that needs to be designed.

If you want to see what our other public documents look like, and the general style we use, you can find examples here:

www.fieldreliefnetwork.org.uk/publications

Industry/Entity Type

Graphic Designer

Font styles to use
Other font styles liked:
• Trebuchet

Colors
acd037

Requirements
Must have
• Short report, modern feel.
• Font: Trebuchet
• Colors: black, white and green (Pantone 38, R (105), G (190), B (40)
Nice to have
• Picture spreads. Full picture on cover (no frames or edges), and a couple of pictures on the inside would help. All photographic material can be found here.
• https://dl.boxcrateusercontent.com/u/73916258/Pictures%20for%20KEL2020.zip

```html
<!DOCTYPE html>
<html lang="en">
<head>
<meta charset="utf-8">
<title>Annual Progress Report – Page 01</title>
<link rel="stylesheet" href="https://fonts.googleapis.com/css2?family=Ubuntu:wght@400;500&display=swap">
<style>
  :root {
    --green: #69be28;
    --green-dark: #4f9a1a;
    --orange: #f08a24;
    --orange-light: #f6a345;
    --orange-deep: #e57b17;
    --ink: #3a3a3a;
    --muted: #7a7a7a;
    --rule: #d6d6d6;
    --paper: #ffffff;
  }
  * { margin: 0; padding: 0; box-sizing: border-box; }
  html, body { width: 853px; height: 1200px; overflow: hidden; background: var(--paper); }
  body { font-family: "Ubuntu", "Trebuchet MS", sans-serif; color: var(--ink); }

  .page { position: relative; width: 853px; height: 1200px; }

  .title-bar {
    position: absolute; left: 0; top: 0; width: 853px; height: 80px;
    background: var(--green);
    border-bottom: 4px solid var(--green-dark);
    display: flex; align-items: center; padding-left: 32px;
  }
  .title-bar h1 { color: #fff; font-weight: 500; font-size: 38px; letter-spacing: 0.2px; }

  .feature-image {
    position: absolute; left: 0; top: 84px; width: 276px; height: 386px;
    background: linear-gradient(135deg, var(--orange-light) 0%, var(--orange) 60%, var(--orange-deep) 100%);
  }

  .body-text p {
    font-size: 16.5px; line-height: 30px; text-align: justify; letter-spacing: 0.3px;
  }
  .intro { position: absolute; left: 296px; top: 96px; width: 534px; }
  .intro p + p { margin-top: 30px; }
  .main { position: absolute; left: 34px; top: 485px; width: 796px; }
  .main p + p { margin-top: 30px; }

  .footer {
    position: absolute; left: 0; bottom: 0; width: 853px; height: 50px;
    border-top: 1px solid var(--rule);
    display: flex; align-items: center; padding: 0 22px 0 20px;
    font-size: 13px; color: var(--muted);
  }
  .page-number { display: flex; align-items: center; gap: 10px; font-size: 16px; }
  .page-number::before { content: ""; width: 4px; height: 26px; background: var(--green); }
  .report-name { margin-left: auto; letter-spacing: 1px; }
  .org-name {
    margin-left: 16px; font-size: 13px; font-weight: 400; color: var(--muted); letter-spacing: 1px;
  }
</style>
</head>
<body>
<div class="page">
  <header class="title-bar"><h1>Title Heading Here</h1></header>

  <div class="feature-image" role="img" aria-label="Report photograph with orange tones"></div>

  <section class="body-text intro">
    <p>Lorem Ipsum is simply dummy text of the printing and typesetting industry. Lorem Ipsum has been the industry's industry. Lorem Ipsum has been the finishLorem Ipsum is simply dummy text of the printing and typesetting industry. Lorem Ipsum has been the industry's industry.</p>
    <p>Lorem Ipsum has been the finishLorem Ipsum is simply dummy text of the printing and typesetting industry. Lorem Ipsum has been the industry's industry. Lorem Ipsum has been the finish</p>
  </section>

  <section class="body-text main">
    <p>Lorem Ipsum is simply dummy text of the printing and typesetting industry. Lorem Ipsum has been the industry's industry. Lorem Ipsum has been the finishLorem Ipsum is simply dummy text of the printing and typesetting industry. Lorem Ipsum has been the industry's industry. Lorem Ipsum has been the finishLorem Ipsum is simply dummy text of the printing and typesetting industry. Lorem Ipsum has been the industry's industry. Lorem Ipsum has been the finishLorem Ipsum is simply dummy text of the printing and typesetting industry. Lorem Ipsum has been the industry's industry. Lorem Ipsum has been the finishLorem Ipsum is simply dummy text of the printing and typesetting industry. Lorem Ipsum has been the industry's industry. Lorem Ipsum has been the finish.</p>
    <p>Lorem Ipsum is simply dummy text of the printing and typesetting industry. Lorem Ipsum has been the industry's industry. Lorem Ipsum has been the finishLorem Ipsum is simply dummy text of the printing and typesetting industry. Lorem Ipsum has been the industry's industry. Lorem Ipsum has been the finishLorem Ipsum is simply dummy text of the printing and typesetting industry. Lorem Ipsum has been the industry's industry. Lorem Ipsum has been the finishLorem Ipsum is simply dummy text of the printing and typesetting industry. Lorem Ipsum has been the industry's industry.</p>
  </section>

  <footer class="footer">
    <span class="page-number">01</span>
    <span class="report-name">FIELD RELIEF NETWORK | ANNUAL PROGRESS REPORT 2014</span>
    <span class="org-name">Field Relief</span>
  </footer>
</div>
</body>
</html>
```